Optometrist/Eye Care Clinic Business card with new logo attached

We are a small, independent eye care clinic in Canada. We have recently updated our logo (as attached), and would like a professional, modern and health care oriented business card to highlight our office details and our optometrist. We'd like to incorporate the blue colours as seen on our logo.

Target Market(s)

demographic: age 35-65 male/female equal

Industry/Entity Type

Health Care

Contact Information for Business Card

Name of clinic: "Marrow Bend Eye Care Optometry"

Font styles to use
Sans Serif

Colors
0355a3

Requirements
Must have
• our website: marrowbendeyecare.com
• Dr Lena Quorvik
• Optometrist
• 217-392 E Halvering Ave
• Vancouver BC V6R 3J8
• P: 604-319-2058
• E: info@marrowbendeyecare.com
Nice to have
• front side: logo/name of clinic as seen on logo attached and website
• backside: logo on the left side, and name/title/address/phone/email

```html
<!DOCTYPE html>
<html lang="en">
<head>
<meta charset="utf-8">
<title>Marrow Bend Eye Care Optometry – Business Card</title>
<link rel="stylesheet" href="https://fonts.googleapis.com/css2?family=Open+Sans:wght@400;600&display=swap">
<style>
  :root {
    --brand-blue: #0355a3;
    --deep-blue: #1b5f9e;
    --mid-blue: #3d8fd6;
    --pale-blue: #d6ebfa;
    --mist: #eef7fd;
    --silver: #c9cdd2;
    --ink: #1f1f1f;
    --logo-ink: #1d5a7e;
    --white: #ffffff;
  }
  * { margin: 0; padding: 0; box-sizing: border-box; }
  html, body { width: 1200px; height: 900px; overflow: hidden; background: var(--white); }
  body { position: relative; font-family: "Open Sans", Arial, sans-serif; color: var(--ink); }

  .card {
    position: absolute;
    overflow: hidden;
    box-shadow: 8px 10px 14px rgba(0,0,0,0.45);
  }
  .card-front { left: 80px; top: 28px; width: 677px; height: 387px; }
  .card-back  { left: 398px; top: 466px; width: 682px; height: 390px; }

  .card-surface { position: absolute; inset: 0; width: 100%; height: 100%; }

  .brand-mark {
    position: absolute;
    text-align: center;
    font-family: "Open Sans", Arial, sans-serif;
    font-weight: 400;
    color: var(--logo-ink);
    line-height: 1;
  }
  .brand-mark .brand-dot {
    display: block;
    margin: 0 auto;
    border-radius: 50%;
    background: var(--logo-ink);
  }
  .brand-line { display: block; white-space: nowrap; }

  .front-brand { left: 238px; top: 32px; width: 200px; }
  .front-brand .brand-dot { width: 90px; height: 90px; margin-bottom: 30px; }
  .front-brand .line-1 { font-size: 19px; letter-spacing: 2px; }
  .front-brand .line-2 { font-size: 26px; letter-spacing: 3px; margin-top: 6px; }
  .front-brand .line-3 { font-size: 12px; letter-spacing: 5px; margin-top: 6px; }

  .front-web {
    position: absolute;
    right: 40px; bottom: 44px;
    font-size: 24px;
    color: var(--white);
  }

  .back-brand { left: 20px; top: 42px; width: 300px; }
  .back-brand .brand-dot { width: 180px; height: 180px; margin-bottom: 26px; }
  .back-brand .line-1 { font-size: 27px; letter-spacing: 3px; }
  .back-brand .line-2 { font-size: 38px; letter-spacing: 4px; margin-top: 8px; }
  .back-brand .line-3 { font-size: 19px; letter-spacing: 7px; margin-top: 8px; }

  .doctor { position: absolute; left: 378px; top: 52px; }
  .doctor-name { font-size: 36px; font-weight: 400; line-height: 1.1; color: var(--ink); }
  .doctor-title { font-size: 19px; margin-top: 2px; color: var(--ink); }
  .doctor-rule {
    position: absolute; left: 380px; top: 124px;
    width: 254px; height: 2px; background: var(--deep-blue);
  }

  .contact-list { position: absolute; left: 378px; top: 154px; list-style: none; }
  .contact-item { display: flex; align-items: flex-start; height: 53px; font-size: 16px; color: var(--ink); }
  .contact-item svg { width: 24px; height: 24px; margin-right: 10px; flex: none; }
  .contact-address { font-size: 16px; line-height: 1.4; }
  .contact-address small { display: block; font-size: 14px; }
</style>
</head>
<body>

<section class="card card-front" aria-label="Business card front">
  <svg class="card-surface" viewBox="0 0 677 387" preserveAspectRatio="none" aria-hidden="true">
    <defs>
      <linearGradient id="front-sky" x1="0" y1="0" x2="1" y2="0.4">
        <stop offset="0" stop-color="#bfe0f6"/>
        <stop offset="0.6" stop-color="#f2f9fe"/>
        <stop offset="1" stop-color="#ffffff"/>
      </linearGradient>
      <linearGradient id="front-sea" x1="0" y1="0" x2="1" y2="1">
        <stop offset="0" stop-color="#1f68bb"/>
        <stop offset="0.6" stop-color="#0e5cb0"/>
        <stop offset="1" stop-color="#3e9fe0"/>
      </linearGradient>
      <linearGradient id="front-steel" x1="0" y1="0" x2="1" y2="0">
        <stop offset="0" stop-color="#e8eaec"/>
        <stop offset="0.35" stop-color="#6d7278"/>
        <stop offset="0.6" stop-color="#dfe2e5"/>
        <stop offset="1" stop-color="#8a9096"/>
      </linearGradient>
    </defs>
    <rect width="677" height="387" fill="url(#front-sky)"/>
    <path d="M0 170 C130 260 280 300 420 255 C520 222 600 200 677 204 L677 387 L0 387 Z" fill="var(--mid-blue)"/>
    <path d="M0 190 C130 275 280 305 420 262 C520 232 600 210 677 212" fill="none" stroke="#ffffff" stroke-width="6"/>
    <path d="M0 205 C130 285 280 310 420 268 C520 240 600 220 677 220" fill="none" stroke="url(#front-steel)" stroke-width="12"/>
    <path d="M0 222 C130 300 280 318 420 276 C520 250 600 230 677 228 L677 387 L0 387 Z" fill="#ffffff"/>
    <path d="M0 232 C130 308 280 326 420 284 C520 258 600 238 677 236 L677 387 L0 387 Z" fill="url(#front-sea)"/>
  </svg>
  <div class="brand-mark front-brand">
    <span class="brand-dot"></span>
    <span class="brand-line line-1">MARROW BEND</span>
    <span class="brand-line line-2">EYE CARE</span>
    <span class="brand-line line-3">OPTOMETRY</span>
  </div>
  <p class="front-web">marrowbendeyecare.com</p>
</section>

<section class="card card-back" aria-label="Business card back">
  <svg class="card-surface" viewBox="0 0 682 390" preserveAspectRatio="none" aria-hidden="true">
    <defs>
      <linearGradient id="back-sky" x1="0" y1="0" x2="1" y2="0.3">
        <stop offset="0" stop-color="#cfe7f8"/>
        <stop offset="0.5" stop-color="#eef7fd"/>
        <stop offset="1" stop-color="#ffffff"/>
      </linearGradient>
    </defs>
    <rect width="682" height="390" fill="url(#back-sky)"/>
    <rect x="324" y="0" width="33" height="390" fill="var(--silver)"/>
    <path d="M324 0 H357 V82 Q357 96 342 100 Q326 96 324 82 Z" fill="var(--brand-blue)"/>
    <path d="M324 390 H357 V312 Q357 298 342 294 Q326 298 324 312 Z" fill="var(--brand-blue)"/>
    <path d="M324 94 Q340 108 357 94 V112 Q340 124 324 112 Z" fill="#ffffff"/>
    <path d="M324 296 Q340 282 357 296 V280 Q340 270 324 280 Z" fill="#ffffff"/>
  </svg>

  <div class="brand-mark back-brand">
    <span class="brand-dot"></span>
    <span class="brand-line line-1">MARROW BEND</span>
    <span class="brand-line line-2">EYE CARE</span>
    <span class="brand-line line-3">OPTOMETRY</span>
  </div>

  <div class="doctor">
    <h1 class="doctor-name">Dr. Lena Quorvik</h1>
    <p class="doctor-title">Optometrist</p>
  </div>
  <div class="doctor-rule"></div>

  <ul class="contact-list">
    <li class="contact-item">
      <svg viewBox="0 0 24 24" aria-hidden="true"><path d="M6 2 L9 2 L11 7 L8.5 9 C9.5 12 12 14.5 15 15.5 L17 13 L22 15 L22 18 C22 20 20 22 18 21.5 C10 20 4 14 2.5 6 C2 4 4 2 6 2 Z" fill="var(--mid-blue)"/></svg>
      <span>604 319 2058</span>
    </li>
    <li class="contact-item">
      <svg viewBox="0 0 24 24" aria-hidden="true"><rect x="1" y="5" width="22" height="14" fill="none" stroke="var(--mid-blue)" stroke-width="2"/><path d="M1 5 L12 13 L23 5" fill="none" stroke="var(--mid-blue)" stroke-width="2"/></svg>
      <span>info@marrowbendeyecare.com</span>
    </li>
    <li class="contact-item">
      <svg viewBox="0 0 24 24" aria-hidden="true"><g fill="none" stroke="var(--mid-blue)" stroke-width="1.6"><circle cx="12" cy="12" r="10"/><ellipse cx="12" cy="12" rx="4.5" ry="10"/><path d="M2 12 H22 M4 6.5 H20 M4 17.5 H20"/></g></svg>
      <span>marrowbendeyecare.com</span>
    </li>
    <li class="contact-item">
      <svg viewBox="0 0 24 24" aria-hidden="true"><path d="M12 1 C7 1 4 4.5 4 9 C4 15 12 23 12 23 C12 23 20 15 20 9 C20 4.5 17 1 12 1 Z" fill="var(--mid-blue)"/><circle cx="12" cy="9" r="3" fill="#ffffff"/></svg>
      <p class="contact-address">217-392 E Halvering Ave<small>Vancouver, British Columbia V6R 3J8</small></p>
    </li>
  </ul>
</section>

</body>
</html>
```